Accounting services

Looking for a Business card & Logo design

company name - QUELM ACCOUNTING & TAXATION SOLUTIONS

name - Corwin Belto

position - Accountant / Business Consultant

email - "undecided"

Tel : (868) 512-0000 / (868) 287-0000

**PUT THESE TO THE BACK**
Accounting - VAT * INCOME/CORP TAX * RETURNS

REGISTRATION - VAT * NIS * Company Registration/Business Plan

```html
<!DOCTYPE html>
<html lang="en">
<head>
<meta charset="UTF-8">
<title>Quelm Accounting &amp; Taxation Solutions — Business Card</title>
<link rel="stylesheet" href="https://fonts.googleapis.com/css2?family=Arimo:wght@400&display=swap">
<style>
  :root {
    --brand-blue: #4169b5;
    --band-grey: #c4c5c8;
    --card-edge: #111111;
    --paper: #ffffff;
    --text-font: "Arimo", Arial, sans-serif;
  }
  * { box-sizing: border-box; margin: 0; padding: 0; }
  html, body {
    width: 1200px;
    height: 769px;
    overflow: hidden;
    background: var(--paper);
  }
  .canvas {
    position: relative;
    width: 1200px;
    height: 769px;
    font-family: var(--text-font);
    color: var(--brand-blue);
  }
  .card {
    position: absolute;
    background: var(--paper);
    border: 3px solid var(--card-edge);
  }
  .card--front { left: 2px; top: 28px; width: 536px; height: 302px; }
  .card--back  { left: 3px; top: 468px; width: 536px; height: 301px; }

  .side-band {
    position: absolute;
    top: 0;
    bottom: 0;
    background: var(--band-grey);
  }
  .card--front .side-band {
    left: 0;
    width: 79px;
    border-right: 3px solid var(--card-edge);
  }
  .card--back .side-band {
    right: 0;
    width: 82px;
    border-left: 3px solid var(--card-edge);
  }

  .company-name {
    position: absolute;
    left: 50%;
    top: 50%;
    transform: translate(-50%, -50%) rotate(-90deg);
    white-space: nowrap;
    font-size: 12.5px;
    letter-spacing: 0.1px;
  }

  .brand-mark {
    position: absolute;
    right: 18px;
    top: 20px;
    font-size: 17px;
    letter-spacing: 1px;
  }

  .identity {
    position: absolute;
    left: 79px;
    right: 0;
    top: 116px;
    text-align: center;
  }
  .identity__name { font-size: 27px; font-weight: 400; line-height: 1.1; }
  .identity__role { font-size: 11px; margin-top: 2px; }

  .contact {
    position: absolute;
    left: 109px;
    top: 220px;
    font-size: 11px;
    list-style: none;
  }
  .contact li + li { margin-top: 19px; }

  .services {
    position: absolute;
    left: 28px;
    top: 217px;
    font-size: 11px;
    list-style: none;
  }
  .services li + li { margin-top: 18px; }

  .brand-display {
    position: absolute;
    left: 706px;
    top: 0;
    width: 494px;
    height: 740px;
    display: flex;
    align-items: center;
    justify-content: center;
    font-size: 104px;
    letter-spacing: 4px;
  }
</style>
</head>
<body>
<main class="canvas">
  <section class="card card--front" aria-label="Business card front">
    <div class="side-band">
      <p class="company-name">QUELM ACCOUNTING &amp; TAXATION SOLUTIONS</p>
    </div>
    <p class="brand-mark">QUELM</p>
    <div class="identity">
      <h1 class="identity__name">Corwin Belto</h1>
      <p class="identity__role">Accountant/Business Consultant</p>
    </div>
    <ul class="contact">
      <li>Email:</li>
      <li>Tel: (868) 512-0000 / (868) 287-0000</li>
    </ul>
  </section>

  <section class="card card--back" aria-label="Business card back">
    <ul class="services">
      <li>Accounting-VAT *INCOME/ CORP TAX* RETURNS</li>
      <li>REGISTRATION-VAT *NIS* Company Registration/ Business Plan</li>
    </ul>
    <div class="side-band"></div>
  </section>

  <p class="brand-display">QUELM</p>
</main>
</body>
</html>
```